Valentine's Day Flyer

We require an A5 size flyer to promote our February parking offer & Giveaway.

Offer:
Book your parking online & Save!
$5 Night/Weekend Parking
$10 Early Bird Parking

Giveaway: Win a $5,000 Diamond Ring!
Every time you book your parking online using Park-n-Hold you get a chance to win!

The final design should contain:
- Valentine's Theme
- Emphasise 'Book your parking online & Save!'

Designers: please visit www.bayvaultlots.com.au for more info on Bayvault Parking & Park-n-Hold

Target Market(s)

18-50 year old drivers

Industry/Entity Type

Parking

```html
<!DOCTYPE html>
<html lang="en">
<head>
<meta charset="utf-8">
<title>Park-n-Hold – Book Online &amp; Save</title>
<link rel="stylesheet" href="https://fonts.googleapis.com/css2?family=Bungee&family=Oswald:wght@700&display=swap">
<style>
  :root {
    --sky: #3cc3e8;
    --teal: #1b6f80;
    --deep: #15404c;
    --paper: #ffffff;
    --mist: #f2f2f2;
    --salmon: #f59a70;
    --coral: #ee5546;
    --ink: #1f1f1f;
    --display: "Bungee", "Arial Black", sans-serif;
    --label: "Oswald", "Arial Narrow", sans-serif;
  }
  html, body {
    margin: 0;
    padding: 0;
    overflow: hidden;
    background: var(--paper);
  }
  .flyer {
    position: relative;
    width: 868px;
    height: 1200px;
    overflow: hidden;
    background: var(--paper);
  }
  .flyer svg { display: block; position: absolute; left: 0; }
  .header { top: 0; }
  .colour-strip { top: 220px; }
  .offer-night { top: 264px; }
  .offer-early { top: 567px; }
  .giveaway { top: 869px; }
  .display { font-family: var(--display); }
  .label { font-family: var(--label); font-weight: 700; }
</style>
</head>
<body>
<main class="flyer">

  <svg class="header" width="868" height="220" viewBox="0 0 868 220">
    <g class="ribbon">
      <polygon points="40,140 125,178 125,140" fill="var(--deep)"/>
      <polygon points="28,48 400,20 400,132 28,162" fill="var(--sky)"/>
      <g transform="rotate(-4.3 214 92)" class="display" fill="var(--paper)" text-anchor="middle">
        <text x="214" y="88" font-size="30" textLength="330" lengthAdjust="spacingAndGlyphs">BOOK YOUR PARKING</text>
        <text x="214" y="128" font-size="30" textLength="330" lengthAdjust="spacingAndGlyphs">ONLINE &amp; SAVE!</text>
      </g>
    </g>
    <g class="brand">
      <text class="label" x="470" y="34" font-size="25" fill="var(--ink)" textLength="260" lengthAdjust="spacingAndGlyphs">BOOK ONLINE &amp; SAVE</text>
      <text class="display" x="470" y="140" font-size="66" fill="var(--teal)" textLength="360" lengthAdjust="spacingAndGlyphs">Park-n-Hold</text>
    </g>
  </svg>

  <svg class="colour-strip" width="868" height="44" viewBox="0 0 868 44">
    <rect x="0" y="0" width="174" height="44" fill="var(--sky)"/>
    <rect x="174" y="0" width="174" height="44" fill="var(--teal)"/>
    <rect x="348" y="0" width="173" height="44" fill="var(--mist)"/>
    <rect x="521" y="0" width="174" height="44" fill="var(--salmon)"/>
    <rect x="695" y="0" width="173" height="44" fill="var(--coral)"/>
  </svg>

  <svg class="offer-night" width="868" height="303" viewBox="0 0 868 303">
    <rect width="868" height="303" fill="var(--salmon)"/>
    <g class="display" fill="var(--coral)" transform="translate(-6 6)">
      <text x="53" y="123" font-size="110" textLength="300" lengthAdjust="spacingAndGlyphs">NIGHT</text>
      <text x="53" y="189" font-size="64" textLength="307" lengthAdjust="spacingAndGlyphs">WEEKEND</text>
      <text x="53" y="267" font-size="98" textLength="307" lengthAdjust="spacingAndGlyphs">PARKING</text>
      <text x="533" y="250" font-size="250" textLength="300" lengthAdjust="spacingAndGlyphs">$5</text>
    </g>
    <g class="display" fill="var(--paper)">
      <text x="53" y="123" font-size="110" textLength="300" lengthAdjust="spacingAndGlyphs">NIGHT</text>
      <text x="53" y="189" font-size="64" textLength="307" lengthAdjust="spacingAndGlyphs">WEEKEND</text>
      <text x="53" y="267" font-size="98" textLength="307" lengthAdjust="spacingAndGlyphs">PARKING</text>
      <text x="533" y="250" font-size="250" textLength="300" lengthAdjust="spacingAndGlyphs">$5</text>
    </g>
    <line x1="447" y1="40" x2="447" y2="275" stroke="var(--coral)" stroke-width="10" stroke-dasharray="16 22"/>
  </svg>

  <svg class="offer-early" width="868" height="302" viewBox="0 0 868 302">
    <rect width="868" height="302" fill="var(--coral)"/>
    <g class="display" fill="var(--salmon)" transform="translate(-6 6)">
      <text x="47" y="246" font-size="255" textLength="390" lengthAdjust="spacingAndGlyphs">$10</text>
      <text x="703" y="113" font-size="92" text-anchor="middle" textLength="260" lengthAdjust="spacingAndGlyphs">EARLY</text>
      <text x="703" y="193" font-size="92" text-anchor="middle" textLength="220" lengthAdjust="spacingAndGlyphs">BIRD</text>
      <text x="703" y="262" font-size="73" text-anchor="middle" textLength="257" lengthAdjust="spacingAndGlyphs">PARKING</text>
    </g>
    <g class="display" fill="var(--paper)">
      <text x="47" y="246" font-size="255" textLength="390" lengthAdjust="spacingAndGlyphs">$10</text>
      <text x="703" y="113" font-size="92" text-anchor="middle" textLength="260" lengthAdjust="spacingAndGlyphs">EARLY</text>
      <text x="703" y="193" font-size="92" text-anchor="middle" textLength="220" lengthAdjust="spacingAndGlyphs">BIRD</text>
      <text x="703" y="262" font-size="73" text-anchor="middle" textLength="257" lengthAdjust="spacingAndGlyphs">PARKING</text>
    </g>
    <line x1="493" y1="40" x2="493" y2="275" stroke="var(--salmon)" stroke-width="10" stroke-dasharray="16 22"/>
  </svg>

  <svg class="giveaway" width="868" height="331" viewBox="0 0 868 331">
    <rect width="868" height="331" fill="var(--teal)"/>
    <text class="display" x="27" y="138" font-size="130" fill="var(--sky)" textLength="626" lengthAdjust="spacingAndGlyphs">GIVEAWAY:</text>
    <rect x="667" y="51" width="133" height="93" rx="10" fill="#2a8da3" role="img" aria-label="Diamond illustration"/>
    <text class="display" x="24" y="224" font-size="54" fill="var(--paper)" textLength="823" lengthAdjust="spacingAndGlyphs">WIN A $5,000 DIAMOND RING!</text>
    <text class="display" x="24" y="272" font-size="38" fill="var(--sky)" textLength="823" lengthAdjust="spacingAndGlyphs">EVERY TIME YOU BOOK YOUR PARKING ONLINE</text>
    <text class="display" x="24" y="316" font-size="38" fill="var(--sky)" textLength="823" lengthAdjust="spacingAndGlyphs">USING PARK-N-HOLD YOU GET A CHANCE TO WIN!</text>
  </svg>

</main>
</body>
</html>
```